Designer Instructions – Updated Referral Program Flyer

(Based on the mock-up in “Brief Layout and Instructions.pdf”)

OVERALL STYLE + LAYOUT

Maintain the same general layout, structure, and flow as the mock-up flyer (front and back).

This is an update of an older flyer, not a full redesign — keep the same sections, proportions, and overall visual feel, but with cleaner, more modern design improvements.

The final flyer should look clean, bold, professional, and high-impact, geared toward realtors, property managers, and contractors who refer work.

FRONT SIDE INSTRUCTIONS
1. Header Section

Remove the Tallow Ridge Builders logo from the top banner.
(Shown on page 1 of the PDF)

2. Main Headline

Keep the same three-line structure:
EARN
UNLIMITED
CASH

Center it, maximize impact, and increase the font size of CASH so all three words match in importance.

Make the headline bold, clean, and the main focal point.

3. Cash Incentive Box

Keep the "$500 minimum OR 10% per referral" box, but upgrade the graphics to look sharper and more modern.

Ensure the wording matches exactly what’s in the mock-up.

4. Premier Partner Program Ribbon

Clean up and modernize the "PREMIER PARTNER PROGRAM" bar while keeping the same position and structure.

Ensure the checkmark badge remains crisp and professional.

5. Supporting Icons Section

Keep the four icons/benefit boxes (Guaranteed Payout, Free Evaluations, Affordable Solutions, Industry Leaders) in the same order.

Update the icons to cleaner, more modern styles — but maintain the same meanings.

Improve alignment and spacing for sharper visual consistency.

6. Remove Icons in Contact Area

At the bottom (“CALL TEXT OR BOOK ONLINE 555-014-2796 TallowRidgeBuilders.example”), remove the phone and internet icons, as noted on page 2 of the PDF.

7. Replace All Images

I (Darnell) will provide all updated stock images separately via email.

Replace the flood/water-damage imagery and roof leak with the new images I send.

Keep image placement and proportions the same as the mock-up.

BACK SIDE INSTRUCTIONS
1. Header Image + “REFER / EARN” Section

Maintain the same large split-image layout (“The more you refer, the more you earn”).

Replace all background imagery with the new assets I will send.

Keep the CASH FLOW image section but modernize the type and spacing.

2. “HOW IT WORKS” Section

Preserve the three-column layout:

Refer Flood, Water & Mold Damage

We Take Care of Everything (evaluations/insurance)

Get Paid to Share

Update images, tighten spacing, and use modern iconography.

3. Remove Phone/Internet Icons

Same as the front side — remove small communication icons and keep only the text/number/URL.

4. Bottom Contact Bar

Keep the blue bar, same wording, same layout — just modernize the style if needed for clarity.

5. Replace All Back-Side Images

Again, I will email you the image assets.

Keep the layout EXACT — just update with higher-quality photos and improved design.

TEXT CONTENT (Keep as-is unless spacing adjustments needed)

All text shown in the PDF should remain exactly the same unless spacing or visual balance requires minor adjustments.
Example from page 3:

“REFER FLOOD, MOLD & CONSTRUCTION JOBS”

“We Schedule a Free Estimate. If Approved, You Get Paid.”

“Everybody Benefits From Referrals”

Everything stays, just refreshed and visually improved.

DESIGN GOALS

Flyer should look high-end and trustworthy, not salesy.

Consistent color theme: blues, whites, yellows, same palette as original.

Use bold, modern fonts with strong readability.

Ensure all headlines pop and all benefit boxes are clean, well-aligned, and evenly spaced.

The final result should feel like a premium referral program flyer for a top-tier restoration/remodel company.

FILES I WILL PROVIDE

I will send the designer:

All replacement stock photos

Any updated logos (if needed)

Original high-resolution version of the mock-up (if available)

Any additional icons preferred

0054AA
0677BA
7BADD7
CADEEF
E8F1F8

• Designer Instructions – Updated Referral Program Flyer (Based on the mock-up in “Brief Layout and Instructions.pdf”) OVERALL STYLE + LAYOUT Maintain the same general layout, structure, and flow as the mock-up flyer (front and back). This is an update of an older flyer, not a full redesign — keep the same sections, proportions, and overall visual feel, but with cleaner, more modern design improvements. The final flyer should look clean, bold, professional, and high-impact, geared toward realtors, property managers, and contractors who refer work. FRONT SIDE INSTRUCTIONS 1. Header Section Remove the Tallow Ridge Builders logo from the top banner. (Shown on page 1 of the PDF) 2. Main Headline Keep the same three-line structure: EARN UNLIMITED CASH Center it, maximize impact, and increase the font size of CASH so all three words match in importance. Make the headline bold, clean, and the main focal point. 3. Cash Incentive Box Keep the "$500 minimum OR 10% per referral" box, but upgrade the graphics to look sharper and more modern. Ensure the wording matches exactly what’s in the mock-up. 4. Premier Partner Program Ribbon Clean up and modernize the "PREMIER PARTNER PROGRAM" bar while keeping the same position and structure. Ensure the checkmark badge remains crisp and professional. 5. Supporting Icons Section Keep the four icons/benefit boxes (Guaranteed Payout, Free Evaluations, Affordable Solutions, Industry Leaders) in the same order. Update the icons to cleaner, more modern styles — but maintain the same meanings. Improve alignment and spacing for sharper visual consistency. 6. Remove Icons in Contact Area At the bottom (“CALL TEXT OR BOOK ONLINE 555-014-2796 TallowRidgeBuilders.example”), remove the phone and internet icons, as noted on page 2 of the PDF. 7. Replace All Images I (Darnell) will provide all updated stock images separately via email. Replace the flood/water-damage imagery and roof leak with the new images I send. Keep image placement and proportions the same as the mock-up. BACK SIDE INSTRUCTIONS 1. Header Image + “REFER / EARN” Section Maintain the same large split-image layout (“The more you refer, the more you earn”). Replace all background imagery with the new assets I will send. Keep the CASH FLOW image section but modernize the type and spacing. 2. “HOW IT WORKS” Section Preserve the three-column layout: Refer Flood, Water & Mold Damage We Take Care of Everything (evaluations/insurance) Get Paid to Share Update images, tighten spacing, and use modern iconography. 3. Remove Phone/Internet Icons Same as the front side — remove small communication icons and keep only the text/number/URL. 4. Bottom Contact Bar Keep the blue bar, same wording, same layout — just modernize the style if needed for clarity. 5. Replace All Back-Side Images Again, I will email you the image assets. Keep the layout EXACT — just update with higher-quality photos and improved design. TEXT CONTENT (Keep as-is unless spacing adjustments needed) All text shown in the PDF should remain exactly the same unless spacing or visual balance requires minor adjustments. Example from page 3: “REFER FLOOD, MOLD & CONSTRUCTION JOBS” “We Schedule a Free Estimate. If Approved, You Get Paid.” “Everybody Benefits From Referrals” Everything stays, just refreshed and visually improved. DESIGN GOALS Flyer should look high-end and trustworthy, not salesy. Consistent color theme: blues, whites, yellows, same palette as original. Use bold, modern fonts with strong readability. Ensure all headlines pop and all benefit boxes are clean, well-aligned, and evenly spaced. The final result should feel like a premium referral program flyer for a top-tier restoration/remodel company. FILES I WILL PROVIDE I will send the designer: All replacement stock photos Any updated logos (if needed) Original high-resolution version of the mock-up (if available) Any additional icons preferred

```html
<!DOCTYPE html>
<html lang="en">
<head>
<meta charset="utf-8">
<title>Referral Program Flyer</title>
<link rel="stylesheet" href="https://fonts.googleapis.com/css2?family=Alfa+Slab+One&family=Poppins:ital,wght@0,400;0,500;0,700;0,800;1,800;1,900&family=Open+Sans:wght@400&display=swap">
<style>
  :root {
    --navy: #22336f;
    --blue-deep: #1c3784;
    --blue-light: #3566b8;
    --yellow: #f8cd14;
    --red: #d63a3a;
    --ink: #1e1a1a;
    --white: #ffffff;
    --panel: #ededee;
    --ring: #c9c9cc;
    --page: #c0dcfc;
    --photo-a: #d9dcdf;
    --photo-b: #9ea4aa;
  }
  * { box-sizing: border-box; margin: 0; padding: 0; }
  html, body { width: 1200px; height: 1000px; overflow: hidden; background: var(--page); }
  .canvas { position: relative; width: 1200px; height: 1000px; }
  .flyer {
    position: absolute; left: 0; top: 112px;
    width: 1680px; height: 1086px;
    transform: scale(0.714286); transform-origin: 0 0;
    font-family: "Poppins", sans-serif; overflow: hidden;
  }
  .flyer-shapes { position: absolute; inset: 0; }
  .photo-area { position: absolute; left: 760px; top: 0; width: 920px; height: 545px; }

  .headline { position: absolute; left: 130px; top: 60px; width: 600px; height: 400px; }
  .headline text { font-family: "Alfa Slab One", serif; text-anchor: middle; }

  .incentive { position: absolute; left: 0; top: 485px; height: 117px; color: var(--white); font-family: "Poppins", sans-serif; font-style: italic; }
  .incentive .amount { position: absolute; left: 74px; top: 2px; font-size: 68px; font-weight: 900; letter-spacing: -2px; line-height: 1.2; }
  .incentive .amount-note { position: absolute; left: 93px; top: 70px; font-size: 24px; font-weight: 800; }
  .incentive .or { position: absolute; left: 280px; top: 16px; font-size: 48px; font-weight: 700; font-style: normal; color: var(--ink); }
  .incentive .percent { position: absolute; left: 386px; top: 12px; font-size: 62px; font-weight: 900; letter-spacing: -2px; }
  .incentive .percent-note { position: absolute; left: 510px; top: 28px; font-size: 27px; font-weight: 800; line-height: 30px; }
  .incentive .percent-note span { display: block; padding-left: 10px; }
  .incentive .percent-note span + span { padding-left: 0; }

  .premier { position: absolute; left: 1025px; top: 435px; width: 430px; text-align: center; font-family: "Open Sans", sans-serif; font-size: 38px; letter-spacing: 18px; color: var(--white); }
  .ribbon { position: absolute; left: 868px; top: 497px; width: 737px; height: 91px; }
  .ribbon-label { position: absolute; top: 14px; font-size: 52px; font-weight: 700; color: var(--white); line-height: 64px; }
  .ribbon-label.left { left: 35px; }
  .ribbon-label.right { left: 425px; }
  .ribbon-badge { position: absolute; left: 306px; top: -5px; width: 90px; height: 100px; }

  .benefits { position: absolute; left: 77px; top: 693px; display: flex; gap: 20px; }
  .benefit { position: relative; width: 368px; height: 252px; background: var(--white); border-radius: 22px; box-shadow: 0 6px 16px rgba(0,0,0,0.10); text-align: center; padding-top: 92px; color: var(--ink); }
  .benefit-icon { position: absolute; left: 50%; top: -60px; width: 124px; height: 124px; margin-left: -62px; border-radius: 50%; background: var(--white); border: 6px solid var(--ring); border-top-color: var(--white); display: flex; align-items: center; justify-content: center; }
  .benefit-icon svg { width: 70px; height: 70px; }
  .benefit h3 { font-size: 32px; font-weight: 800; line-height: 41px; color: var(--navy); letter-spacing: 0.5px; }
  .benefit p { font-size: 20px; line-height: 27px; margin-top: 4px; letter-spacing: 0.5px; }

  .contact-call { position: absolute; left: 60px; top: 1010px; font-size: 27px; font-weight: 800; color: var(--navy); letter-spacing: 0.5px; }
  .contact-call .soft { font-weight: 400; }
  .contact-phone { position: absolute; left: 626px; top: 992px; font-size: 58px; font-weight: 800; color: var(--white); letter-spacing: -0.5px; line-height: 80px; }
  .contact-web { position: absolute; left: 1168px; top: 1011px; font-size: 28px; font-weight: 400; color: var(--white); letter-spacing: 0.5px; }
</style>
</head>
<body>
<div class="canvas">
  <section class="flyer" aria-label="Referral partner program flyer">
    <svg class="flyer-shapes" viewBox="0 0 1680 1086" width="1680" height="1086" aria-hidden="true">
      <defs>
        <radialGradient id="burst" cx="430" cy="300" r="620" gradientUnits="userSpaceOnUse">
          <stop offset="0" stop-color="#3f78cc"/>
          <stop offset="0.55" stop-color="#24479a"/>
          <stop offset="1" stop-color="#1c3784"/>
        </radialGradient>
      </defs>
      <rect x="0" y="545" width="1680" height="432" fill="var(--panel)"/>
      <polygon points="0,0 802,0 912,270 802,545 0,545" fill="var(--yellow)"/>
      <polygon points="0,0 768,0 878,270 768,545 0,545" fill="#e8e8ea"/>
      <polygon points="0,0 745,0 855,270 745,545 0,545" fill="url(#burst)"/>
      <polygon points="0,485 718,485 670,602 0,602" fill="var(--red)"/>
      <polygon points="262,510 375,510 352,578 245,578" fill="var(--white)"/>
      <polygon points="0,977 558,977 518,1086 0,1086" fill="var(--yellow)"/>
      <polygon points="558,977 578,977 538,1086 518,1086" fill="#ececee"/>
      <polygon points="578,977 1680,977 1680,1086 538,1086" fill="var(--navy)"/>
      <rect x="1106" y="1000" width="3" height="64" fill="var(--white)"/>
    </svg>

    <div class="photo-area" role="img" aria-label="Photo of a bright modern open-plan living room and kitchen with grey sofas and tall windows"
         style="background: linear-gradient(160deg, var(--photo-a) 0%, #c3c7cb 45%, var(--photo-b) 100%);"></div>

    <svg class="headline" viewBox="0 0 600 400" aria-label="Earn unlimited cash" role="img">
      <g font-size="118" transform="skewX(-6)">
        <text x="320" y="140" fill="var(--white)" stroke="var(--white)" stroke-width="46" stroke-linejoin="round">EARN</text>
        <text x="320" y="140" fill="var(--yellow)" stroke="var(--ink)" stroke-width="22" stroke-linejoin="round" paint-order="stroke">EARN</text>
      </g>
      <g font-size="86" transform="skewX(-6)">
        <text x="328" y="230" fill="var(--white)" stroke="var(--white)" stroke-width="46" stroke-linejoin="round">UNLIMITED</text>
        <text x="328" y="230" fill="var(--white)" stroke="var(--ink)" stroke-width="22" stroke-linejoin="round" paint-order="stroke">UNLIMITED</text>
      </g>
      <g font-size="118" transform="skewX(-6)">
        <text x="340" y="335" fill="var(--white)" stroke="var(--white)" stroke-width="46" stroke-linejoin="round">CA$H</text>
        <text x="340" y="335" fill="var(--yellow)" stroke="var(--ink)" stroke-width="22" stroke-linejoin="round" paint-order="stroke">CA$H</text>
      </g>
    </svg>

    <div class="incentive">
      <span class="amount">$500</span>
      <span class="amount-note">MINIMUM</span>
      <span class="or">or</span>
      <span class="percent">10%</span>
      <span class="percent-note"><span>PER</span><span>REFERRAL</span></span>
    </div>

    <div class="premier">PREMIER</div>
    <div class="ribbon">
      <svg width="737" height="91" viewBox="0 0 737 91" aria-hidden="true" style="position:absolute;left:0;top:0">
        <path d="M45.5 0 H360 V91 H45.5 A45.5 45.5 0 0 1 45.5 0 Z" fill="var(--red)"/>
        <path d="M340 0 H691.5 A45.5 45.5 0 0 1 691.5 91 H340 Z" fill="var(--ink)"/>
      </svg>
      <span class="ribbon-label left">PARTNER</span>
      <svg class="ribbon-badge" viewBox="0 0 90 100" aria-hidden="true">
        <path d="M45 4 C60 14 74 16 86 14 V50 C86 74 66 90 45 98 C24 90 4 74 4 50 V14 C16 16 30 14 45 4 Z" fill="var(--white)"/>
        <path d="M22 50 L39 66 L70 30" fill="none" stroke="var(--red)" stroke-width="11" stroke-linecap="round" stroke-linejoin="round"/>
      </svg>
      <span class="ribbon-label right">PROGRAM</span>
    </div>

    <div class="benefits">
      <article class="benefit">
        <div class="benefit-icon">
          <svg viewBox="0 0 70 70" aria-hidden="true">
            <path d="M35 3 l8 6 10-1 3 10 9 5-3 10 3 10-9 5-3 10-10-1-8 6-8-6-10 1-3-10-9-5 3-10-3-10 9-5 3-10 10 1z" fill="var(--navy)"/>
            <circle cx="35" cy="35" r="18" fill="none" stroke="var(--white)" stroke-width="4"/>
            <path d="M27 35 l6 6 11-12" fill="none" stroke="var(--white)" stroke-width="4.5" stroke-linecap="round" stroke-linejoin="round"/>
          </svg>
        </div>
        <h3>GUARANTEED<br>PAYOUT</h3>
        <p>Minimum $500 or 10% of<br>Total Invoice Paid Fast</p>
      </article>
      <article class="benefit">
        <div class="benefit-icon">
          <svg viewBox="0 0 70 70" aria-hidden="true">
            <rect x="6" y="4" width="40" height="60" rx="4" fill="var(--navy)"/>
            <rect x="12" y="10" width="28" height="12" fill="var(--white)"/>
            <g fill="var(--white)">
              <rect x="12" y="28" width="7" height="7"/><rect x="22" y="28" width="7" height="7"/><rect x="32" y="28" width="7" height="7"/>
              <rect x="12" y="39" width="7" height="7"/><rect x="22" y="39" width="7" height="7"/><rect x="32" y="39" width="7" height="7"/>
              <rect x="12" y="50" width="7" height="7"/><rect x="22" y="50" width="7" height="7"/>
            </g>
            <circle cx="55" cy="42" r="11" fill="var(--white)" stroke="var(--navy)" stroke-width="3"/>
            <text x="55" y="47" font-size="14" font-weight="700" text-anchor="middle" fill="var(--navy)" font-family="Poppins, sans-serif">$</text>
            <rect x="42" y="55" width="26" height="10" rx="3" fill="var(--navy)"/>
          </svg>
        </div>
        <h3>FREE<br>ESTIMATES</h3>
        <p>Fast &amp; Free Inspections<br>&amp; Written Estimates</p>
      </article>
      <article class="benefit">
        <div class="benefit-icon">
          <svg viewBox="0 0 70 70" aria-hidden="true">
            <circle cx="40" cy="22" r="17" fill="var(--navy)"/>
            <text x="40" y="30" font-size="22" font-weight="800" text-anchor="middle" fill="var(--white)" font-family="Poppins, sans-serif">$</text>
            <rect x="6" y="42" width="11" height="22" rx="2" fill="var(--navy)"/>
            <path d="M19 46 h18 c5 0 5 7 0 7 h-10 h14 l18-10 c5-3 9 3 5 6 l-22 15 h-23z" fill="var(--navy)"/>
          </svg>
        </div>
        <h3>AFFORDABLE<br>SOLUTIONS</h3>
        <p>Lowest Out of Pocket Costs<br>for Your Customers</p>
      </article>
      <article class="benefit">
        <div class="benefit-icon">
          <svg viewBox="0 0 70 70" aria-hidden="true">
            <circle cx="35" cy="18" r="13" fill="none" stroke="var(--navy)" stroke-width="5" stroke-dasharray="5 3"/>
            <circle cx="35" cy="18" r="7" fill="var(--navy)"/>
            <circle cx="14" cy="30" r="6" fill="var(--navy)"/>
            <circle cx="56" cy="30" r="6" fill="var(--navy)"/>
            <path d="M3 48 a11 10 0 0 1 22 0z M45 48 a11 10 0 0 1 22 0z" fill="var(--navy)"/>
            <path d="M22 50 a13 12 0 0 1 26 0z" fill="var(--navy)"/>
            <circle cx="35" cy="53" r="6" fill="var(--navy)"/>
            <path d="M24 68 a11 10 0 0 1 22 0z" fill="var(--navy)"/>
          </svg>
        </div>
        <h3>INDUSTRY<br>LEADERS</h3>
        <p>Licensed &amp; Certified Experts<br>Provide 100% Guarante</p>
      </article>
    </div>

    <div class="contact-call">CALL, TEXT <span class="soft">OR</span> BOOK ONLINE</div>
    <div class="contact-phone">555-014-2796</div>
    <div class="contact-web">www.TallowRidgeBuilders.example</div>
  </section>
</div>
</body>
</html>
```